We need a website that entices australia's workers to sign up to help protect their industry and their jobs. The key message is "Steady Ground Works" and that headline / tagline should feature prominently on the site.

In terms of style I lack the current 'scrolling' style (see example http://www.fieldmarkweb.ca )

The site must dynamically for mobile platforms. It must also use Quenda or Paperloft as CMS so is client editable.

The attached logo is the basis for the design and the name of the organisation is the Enduring Progress Council. Please make an allowance for an iframe embed (min height 650px) see attached sample.

It should also have a subscriber sign up for that connects with Mailbridge Relay

Attached text for front page is DRAFT ONLY

Target Market(s)

Working class australians, (eg miners, farmers, factory workers, etc)

Industry/Entity Type

Industry

Coding

Coded - Design and coding required

Number of Pages Required

4 page

Requirements
Must have
• An editable CMS
• Subscription form connecting with Mailbridge Relay (see https://kovalpint.sendquill.com/help/topic.aspx?t=13)
• Must resize for mobile
• Must allow for an iframe
Nice to have
• It must have a friendly feel but strong, not 'girly' though should not alienate women
Should not have
• Images that are not australian
• Images that do not have the appropriate rights to use

```html
<!DOCTYPE html>
<html lang="en">
<head>
<meta charset="utf-8">
<title>Steady Ground Works</title>
<link href="https://fonts.googleapis.com/css2?family=Open+Sans:ital,wght@0,300;0,400;0,600;0,700;1,400;1,700&display=swap" rel="stylesheet">
<style>
:root{
  --orange:#f15a29;
  --amber:#f7941d;
  --ink:#2b2b2b;
  --grey-text:#7a7a7a;
  --soft:#f2f2f2;
  --white:#ffffff;
  --field-line:#d5d5d5;
}
*{box-sizing:border-box;margin:0;padding:0}
html,body{width:680px;height:1200px;overflow:hidden}
body{font-family:"Open Sans",Arial,sans-serif;color:var(--ink);background:var(--white);position:relative}
a{text-decoration:none}
.page{position:relative;width:680px;height:1200px;overflow:hidden}

/* hero */
.hero{position:absolute;left:0;top:0;width:680px;height:330px;
  background:linear-gradient(180deg,#0f1a33 0%,#1b2b4d 45%,#2a3550 62%,#5a4030 74%,#1a2238 86%,#0e1526 100%)}
.hero-art{position:absolute;inset:0}
.topbar{position:absolute;left:0;top:0;width:680px;height:54px}
.brand{position:absolute;left:126px;top:16px;display:flex;align-items:center;gap:7px;
  font-size:8.5px;font-weight:600;color:var(--amber);line-height:1.15;text-transform:uppercase;letter-spacing:.2px}
.brand-dot{width:22px;height:22px;border-radius:50%;background:var(--amber)}
.nav{position:absolute;right:120px;top:21px;display:flex;gap:20px;list-style:none}
.nav a{font-size:9px;color:var(--white)}
.nav a.current{color:var(--amber)}
.hero-title{position:absolute;top:101px;width:100%;text-align:center;color:var(--white);
  font-size:27px;font-weight:700;letter-spacing:.5px}
.hero-sub{position:absolute;top:140px;width:100%;text-align:center;color:#e6e6e6;font-size:15px;line-height:1.4;font-weight:300}
.btn{display:inline-block;border:1px solid var(--orange);color:var(--orange);font-size:8.5px;font-weight:700;
  text-transform:uppercase;padding:5px 10px;letter-spacing:.3px;background:transparent;text-decoration:none}
.hero .btn{position:absolute;left:258px;top:216px}

/* message */
.message{position:absolute;left:0;top:290px;width:680px;height:180px;background:var(--white);
  clip-path:polygon(0 0,100% 42px,100% 100%,0 100%)}
.message-inner{position:absolute;left:148px;top:52px;width:390px}
.message h2{font-size:10.5px;font-weight:700;font-style:italic;text-transform:uppercase;line-height:1.35;color:var(--ink)}
.message p{margin-top:8px;font-size:6.5px;line-height:1.6;color:var(--grey-text);text-transform:uppercase}

/* risks */
.risks{position:absolute;left:0;top:410px;width:680px;height:230px;background:var(--white);
  clip-path:polygon(0 40px,100% 18px,100% 100%,0 100%)}
.risks-line{position:absolute;left:0;top:410px;width:680px;height:230px;background:var(--soft);
  clip-path:polygon(0 38px,100% 16px,100% 18px,0 40px)}
.people{position:absolute;left:210px;top:472px;width:46px;height:44px;border-radius:8px;background:var(--orange)}
.pledge{position:absolute;left:150px;top:526px;width:166px;text-align:center;font-size:9.5px;font-weight:700;
  font-style:italic;color:var(--orange);line-height:1.32}
.risk-list{position:absolute;left:355px;top:466px;width:200px}
.risk-list h3{font-size:9px;font-weight:700;font-style:italic;color:var(--amber);text-transform:uppercase;margin-bottom:8px}
.risk-list ul{list-style:none}
.risk-list li{display:flex;gap:6px;font-size:7.5px;line-height:1.3;color:var(--ink);margin-bottom:9px}
.risk-list svg{flex:none;width:10px;height:10px;margin-top:1px}

/* email */
.email{position:absolute;left:0;top:600px;width:680px;height:270px;background:var(--white);
  clip-path:polygon(0 0,100% 36px,100% 100%,0 100%)}
.email-band{position:absolute;left:0;top:590px;width:680px;height:280px;background:var(--soft);
  clip-path:polygon(0 10px,100% 46px,100% 100%,0 100%)}
.email-inner{position:absolute;left:150px;top:653px;width:380px;text-align:center}
.email-inner h2{font-size:14px;font-weight:700;color:var(--ink);text-transform:uppercase}
.email-inner h2 span{font-weight:400}
.email-inner p{margin-top:6px;font-size:6.5px;line-height:1.6;color:var(--grey-text);text-transform:uppercase;text-align:left}
.email-inner .cue{margin-top:6px;text-align:center;color:var(--orange);font-weight:600}
.signup{position:absolute;left:150px;top:720px;width:380px;display:grid;grid-template-columns:185px 185px;gap:7px 10px}
.field{height:19px;border:1px solid var(--field-line);border-radius:3px;background:var(--white);
  font-size:7.5px;font-style:italic;color:#999;padding:4px 7px;position:relative}
.field.select::after{content:"";position:absolute;right:7px;top:7px;border:4px solid transparent;border-top:5px solid #333}
.signup .btn{grid-column:1 / span 2;justify-self:center;margin-top:16px;background:var(--white);padding:5px 14px}

/* start band */
.start{position:absolute;left:0;top:867px;width:680px;height:140px;background:var(--orange);text-align:center;color:var(--white)}
.start h2{margin-top:27px;font-size:19px;font-weight:400;text-transform:uppercase}
.start h2 strong{font-weight:700}
.start p{width:390px;margin:6px auto 0;font-size:7px;line-height:1.55;text-transform:uppercase}
.start .btn{margin-top:14px;border-color:var(--white);color:var(--white)}

/* words */
.words{position:absolute;left:0;top:1007px;width:680px;height:148px;background:var(--soft)}
.words h2{margin-top:35px;text-align:center;font-size:14px;font-weight:700;text-transform:uppercase}
.words h2 span{font-weight:400}
.words p{width:384px;margin:8px auto 0;font-size:7.3px;line-height:1.5;color:#666}
.words p + p{margin-top:8px}

.footer{position:absolute;left:0;top:1155px;width:680px;height:45px;background:var(--white);
  text-align:center;font-size:7.5px;color:#555;padding-top:18px}
</style>
</head>
<body>
<div class="page">

  <header class="hero">
    <div class="hero-art" role="img" aria-label="Night photograph of a lit bridge and city skyline over the water"></div>
    <div class="topbar">
      <div class="brand"><span class="brand-dot"></span><span>Steady Ground<br>Works</span></div>
      <ul class="nav">
        <li><a class="current" href="#">Take Action</a></li>
        <li><a href="#">About</a></li>
        <li><a href="#">Facts</a></li>
        <li><a href="#">News</a></li>
        <li><a href="#">Contact</a></li>
      </ul>
    </div>
    <h1 class="hero-title">MY FAMILY COMES FIRST</h1>
    <p class="hero-sub">I care for the environment – but not at the cost of my job,<br>our savings or our retirement</p>
    <a class="btn" href="#">Take action to protect your family</a>
  </header>

  <section class="message">
    <div class="message-inner">
      <h2>The Greenies want your bank and your super fund to stop investing in mining, agriculture and other industries that are the backbone of Australia.</h2>
      <p>While they are trying to do good, if they are successful their actions will severely impact the lives of everyday Australians. Any loss of investment in Australian industries will have knock on effects for you, your family and your community.</p>
    </div>
  </section>

  <div class="risks-line"></div>
  <section class="risks"></section>
  <div class="people" role="img" aria-label="Illustration of two workers talking"></div>
  <p class="pledge">Tell your bank and super fund you do NOT want them to divest out of Australian industry. Tell them you want to keep Australia strong</p>
  <div class="risk-list">
    <h3>This could</h3>
    <ul>
      <li><svg viewBox="0 0 10 10"><circle cx="5" cy="5" r="4.3" fill="none" stroke="#333" stroke-width="1"/><path d="M2.8 5.1l1.6 1.6 3-3.3" fill="none" stroke="#333" stroke-width="1.1"/></svg>Cost you your job as less investment means less jobs</li>
      <li><svg viewBox="0 0 10 10"><circle cx="5" cy="5" r="4.3" fill="none" stroke="#333" stroke-width="1"/><path d="M2.8 5.1l1.6 1.6 3-3.3" fill="none" stroke="#333" stroke-width="1.1"/></svg>Give you less to retire on as your superannuation fund gets strong returns from investment</li>
      <li><svg viewBox="0 0 10 10"><circle cx="5" cy="5" r="4.3" fill="none" stroke="#333" stroke-width="1"/><path d="M2.8 5.1l1.6 1.6 3-3.3" fill="none" stroke="#333" stroke-width="1.1"/></svg>Reduce your hard earned savings</li>
      <li><svg viewBox="0 0 10 10"><circle cx="5" cy="5" r="4.3" fill="none" stroke="#333" stroke-width="1"/><path d="M2.8 5.1l1.6 1.6 3-3.3" fill="none" stroke="#333" stroke-width="1.1"/></svg>Impact communities that rely on industry</li>
      <li><svg viewBox="0 0 10 10"><circle cx="5" cy="5" r="4.3" fill="none" stroke="#333" stroke-width="1"/><path d="M2.8 5.1l1.6 1.6 3-3.3" fill="none" stroke="#333" stroke-width="1.1"/></svg>Not help the environment at all</li>
    </ul>
  </div>

  <div class="email-band"></div>
  <section class="email"></section>
  <div class="email-inner">
    <h2>Email your bank <span>- It's easy, click here</span></h2>
    <p>Take a few moments to contact your bank and let them know you do not want them to divest from Australian industry. Here's your opportunity to be heard. Your voice will make a difference.</p>
    <p class="cue">To get started please fill in your name and email address</p>
  </div>
  <form class="signup">
    <div class="field">First Name</div>
    <div class="field">Family Name</div>
    <div class="field">Email Address</div>
    <div class="field select">Select Bank</div>
    <div class="field select">Super Fund</div>
    <div></div>
    <a class="btn" href="#">Submit</a>
  </form>

  <section class="start">
    <h2><strong>It's easy</strong> to get started</h2>
    <p>We have developed an advocacy centre — a place where you can send a letter or email to your bank, super fund, MP or your newspaper, share information online with your friends via social media.</p>
    <a class="btn" href="#">Get it now</a>
  </section>

  <section class="words">
    <h2>Some words <span>from us</span></h2>
    <p>Nulla vitae elit libero, a pharetra augue. Donec sed odio dui. Vestibulum id ligula porta felis euismod semper. Aenean lacinia bibendum nulla sed consectetur. Lorem ipsum dolor sit amet, consectetur adipiscing elit.</p>
    <p>Integer posuere erat a ante venenatis dapibus posuere velit aliquet. Vestibulum id ligula porta felis euismod semper. Donec ullamcorper nulla non metus auctor fringilla. Cum sociis natoque penatibus et magnis dis parturient montes, nascetur ridiculus mus. Maecenas sed diam eget risus varius blandit sit amet non magna.</p>
  </section>

  <footer class="footer">© 2015 Steady Ground Works. All rights reserved</footer>
</div>
</body>
</html>
```